I need a business card for myself, being a proprietor of a funeral parlor based in Manila. I'd like the card to have either of the following:
White Font on Black Background
or
Black Font on White Background
No logo is needed however I will appreciate any efforts to show a symbol of eternal happiness, aptly designed with above mentioned colors in mind.
Company name, address and contact on the lower right corner.
Logo or symbol anywhere.
Quillstone Funeral Services
+639174826351
darvik4521@pelmora.com
corner of Brisco Avenue and Velhurst Street
Makati City, Philippines
Thank you.
Update: Please include a small dove in your design. You are free to choose where you would like it on the card.

```html
<!DOCTYPE html>
<html lang="en">
<head>
<meta charset="utf-8">
<title>Quillstone Funeral Services — Business Card</title>
<link rel="stylesheet" href="https://fonts.googleapis.com/css2?family=Libre+Baskerville:wght@700&family=Questrial&display=swap">
<style>
  :root {
    --canvas-bg: #e9e7e3;
    --card-white: #ffffff;
    --card-black: #050505;
    --ink: #111111;
    --symbol-tone: #f2f2f2;
  }
  html, body {
    margin: 0;
    padding: 0;
    width: 1200px;
    height: 1024px;
    overflow: hidden;
    background: var(--canvas-bg);
  }
  .canvas {
    position: relative;
    width: 1200px;
    height: 1024px;
  }
  .card {
    position: absolute;
    left: 140px;
    top: 249px;
    width: 920px;
    height: 526px;
    background: var(--card-white);
    overflow: hidden;
    box-shadow: 0 6px 24px rgba(0,0,0,0.18);
  }
  .card__wave {
    position: absolute;
    inset: 0;
    width: 920px;
    height: 526px;
  }
  .card__wave path { fill: var(--card-black); }
  .card__symbol {
    position: absolute;
    left: 130px;
    top: 205px;
    width: 170px;
    height: 170px;
    background: var(--symbol-tone);
  }
  .card__details {
    position: absolute;
    left: 515px;
    top: 70px;
    width: 380px;
    color: var(--ink);
  }
  .company-name {
    margin: 0 0 54px;
    font-family: "Libre Baskerville", Georgia, serif;
    font-weight: 700;
    font-size: 25px;
    letter-spacing: -0.3px;
    white-space: nowrap;
  }
  .contact-list {
    list-style: none;
    margin: 0;
    padding: 0;
    font-family: "Questrial", "Century Gothic", sans-serif;
    font-size: 21px;
    line-height: 31px;
  }
  .contact-list li {
    display: flex;
    align-items: flex-start;
  }
  .contact-icon {
    flex: none;
    width: 17px;
    height: 17px;
    margin: 7px 11px 0 0;
  }
  .contact-icon * { fill: var(--ink); }
  .contact-address span { display: block; }
</style>
</head>
<body>
<main class="canvas">
  <article class="card">
    <svg class="card__wave" viewBox="0 0 920 526" aria-hidden="true">
      <path d="M0 0 H350 C395 110 475 190 475 300 C475 400 435 470 435 526 H0 Z"/>
    </svg>
    <div class="card__symbol" role="img" aria-label="Endless knot symbol of eternal happiness, white on black"></div>
    <section class="card__details">
      <h1 class="company-name">Quillstone Funeral Services</h1>
      <ul class="contact-list">
        <li>
          <svg class="contact-icon" viewBox="0 0 18 18" aria-hidden="true">
            <path d="M9 0a9 9 0 1 0 0.01 0Zm0 2a7 7 0 1 1-0.01 0Z"/>
            <path d="M6 4.5l1.6 0.2 0.6 2.3-1 0.9a6 6 0 0 0 2.8 2.8l0.9-1 2.3 0.6 0.2 1.6c-0.6 0.9-1.6 1.2-2.6 0.9A8 8 0 0 1 5.1 7.1C4.8 6.1 5.1 5.1 6 4.5Z"/>
          </svg>
          <span>63 917 482 6351</span>
        </li>
        <li>
          <svg class="contact-icon" viewBox="0 0 18 18" aria-hidden="true">
            <path d="M9 0a9 9 0 0 0 0 18h3v-2H9a7 7 0 1 1 7-7v1a1.5 1.5 0 0 1-3 0V9a4 4 0 1 0-1.2 2.9A3.5 3.5 0 0 0 18 10V9a9 9 0 0 0-9-9Zm0 11a2 2 0 1 1 0-4 2 2 0 0 1 0 4Z"/>
          </svg>
          <span>darvik4521@pelmora.com</span>
        </li>
        <li>
          <svg class="contact-icon" viewBox="0 0 18 18" aria-hidden="true">
            <path d="M9 0a6 6 0 0 0-6 6c0 4.5 6 12 6 12s6-7.5 6-12a6 6 0 0 0-6-6Zm0 8.5a2.5 2.5 0 1 1 0-5 2.5 2.5 0 0 1 0 5Z"/>
          </svg>
          <span class="contact-address">
            <span>Corner of Brisco Avenue and</span>
            <span>Velhurst Street Makati City</span>
            <span>Philippines</span>
          </span>
        </li>
      </ul>
    </section>
  </article>
</main>
</body>
</html>
```